Amber Hollow Productions

I need a business card design for a new freelance film production company using or incorporating the logo:
I want the card to be creative, minimal, yet professional. Feel free to use a variety of different shapes and sizes/ textures for the card.

Industry/Entity Type

Film Production

```html
<!DOCTYPE html>
<html lang="en">
<head>
<meta charset="utf-8">
<title>Amber Hollow Productions — Business Card</title>
<link href="https://fonts.googleapis.com/css2?family=Questrial&display=swap" rel="stylesheet">
<style>
  :root {
    --brand-blue: #0f4ff6;
    --paper: #ffffff;
    --slate: #7b828a;
    --slate-light: #c9ccd0;
    --backdrop: #262626;
  }
  * { box-sizing: border-box; margin: 0; padding: 0; }
  html, body {
    width: 1200px; height: 1062px; overflow: hidden;
    background: var(--backdrop);
    font-family: "Questrial", "Century Gothic", sans-serif;
  }
  .card {
    position: absolute;
    width: 580px; height: 332px;
    border-radius: 22px;
    overflow: hidden;
    box-shadow: 0 14px 30px rgba(0,0,0,.45);
  }

  /* ---------- front ---------- */
  .card-front { left: 70px; top: 110px; background: var(--paper); }
  .front-band {
    position: absolute; left: 0; right: 0; top: 150px; height: 146px;
    background: var(--brand-blue);
    border-top: 4px solid var(--slate-light);
  }
  .front-foot {
    position: absolute; left: 0; right: 0; bottom: 0; height: 36px;
    background: var(--paper);
    border-top: 3px solid var(--slate-light);
  }
  .front-brand {
    position: absolute; left: 0; right: 0; top: 56px;
    display: flex; justify-content: center;
    color: var(--brand-blue);
  }
  .brand-name {
    display: inline-flex; align-items: center; gap: 10px;
    white-space: nowrap;
    font-size: 24px; letter-spacing: 1px; text-transform: uppercase;
  }
  .brand-mark { width: 18px; height: 18px; background: currentColor; flex: none; }
  .pointer {
    position: absolute; left: 40px; top: 154px;
    width: 0; height: 0;
    border-left: 14px solid transparent; border-right: 14px solid transparent;
    border-top: 18px solid var(--slate);
  }
  .person { position: absolute; left: 40px; top: 196px; }
  .person-name { color: var(--paper); font-size: 22px; letter-spacing: .5px; }
  .person-role { color: var(--slate); font-size: 15px; margin-top: 2px; }
  .divider {
    position: absolute; left: 285px; top: 150px; width: 2px; height: 146px;
  }
  .contact {
    position: absolute; left: 318px; top: 160px; right: 20px;
    color: var(--paper); font-size: 10.5px; line-height: 1.35;
  }
  .contact-address { margin-bottom: 6px; }
  .contact-list { list-style: none; }
  .contact-list li { display: flex; align-items: center; gap: 8px; margin-bottom: 4px; }
  .contact-icon { width: 13px; height: 13px; flex: none; }

  /* ---------- back ---------- */
  .card-back {
    left: 550px; top: 600px; background: var(--brand-blue);
    color: var(--paper); text-align: center;
  }
  .back-brand {
    position: absolute; left: 0; right: 0; top: 120px;
    display: flex; justify-content: center;
  }
  .back-brand .brand-name { font-size: 28px; gap: 12px; letter-spacing: 1.5px; }
  .back-brand .brand-mark { width: 22px; height: 22px; }
  .back-web {
    position: absolute; left: 0; right: 0; bottom: 48px;
    font-size: 20px; letter-spacing: 3px; white-space: nowrap;
  }
</style>
</head>
<body>

<section class="card card-front" aria-label="Business card front">
  <div class="front-band"></div>
  <div class="front-foot"></div>
  <div class="front-brand">
    <span class="brand-name"><span class="brand-mark"></span>Amber Hollow Productions</span>
  </div>
  <div class="pointer"></div>
  <div class="person">
    <p class="person-name">Ravi Mehta</p>
    <p class="person-role">manager</p>
  </div>
  <svg class="divider" viewBox="0 0 2 146" preserveAspectRatio="none" aria-hidden="true">
    <line x1="1" y1="10" x2="1" y2="136" stroke="#ffffff" stroke-opacity=".6" stroke-width="1"/>
  </svg>
  <div class="contact">
    <p class="contact-address">4410 Lakeview Lane Riverside Park<br>Northfield road 2210</p>
    <ul class="contact-list">
      <li>
        <svg class="contact-icon" viewBox="0 0 16 16" aria-hidden="true"><rect x="4" y="1" width="8" height="14" rx="2" fill="none" stroke="#fff" stroke-width="1.5"/><circle cx="8" cy="12.5" r="1" fill="#fff"/></svg>
        555-014-2086
      </li>
      <li>
        <svg class="contact-icon" viewBox="0 0 16 16" aria-hidden="true"><path d="M4 2l2 3-1.5 1.5a8 8 0 0 0 5 5L11 10l3 2-1 2.5C7 14 2 9 1.5 3z" fill="#fff"/></svg>
        555-014-2086
      </li>
      <li>
        <svg class="contact-icon" viewBox="0 0 16 16" aria-hidden="true"><rect x="1.5" y="3.5" width="13" height="9" fill="none" stroke="#fff" stroke-width="1.5"/><path d="M1.5 3.5l6.5 5 6.5-5" fill="none" stroke="#fff" stroke-width="1.5"/></svg>
        hello@amberhollowproductions.com
      </li>
      <li>
        <svg class="contact-icon" viewBox="0 0 16 16" aria-hidden="true"><circle cx="8" cy="8" r="6.5" fill="none" stroke="#fff" stroke-width="1.3"/><ellipse cx="8" cy="8" rx="3" ry="6.5" fill="none" stroke="#fff" stroke-width="1.1"/><line x1="1.5" y1="8" x2="14.5" y2="8" stroke="#fff" stroke-width="1.1"/></svg>
        www.amberhollowproductions.com
      </li>
    </ul>
  </div>
</section>

<section class="card card-back" aria-label="Business card back">
  <div class="back-brand">
    <span class="brand-name"><span class="brand-mark"></span>Amber Hollow Productions</span>
  </div>
  <p class="back-web">www.amberhollowproductions.com</p>
</section>

</body>
</html>
```